依頼詳細
人工知能(AI)というデジタルでクールなイメージと、教育というアナログで優しいイメージを合わせもった雰囲気のWebサイトを構築したいと考えています。
海外のデザイナーにたたき台となるデザインをしていただいたのですが、やはり日本のデザインとは異なるところが多くあり、日本のデザイナーさんに再度依頼しようと決めました。
他の案件と比べるとたたき台となるWebデザインや営業用のフライヤーまでそろっていますので、色やデザインの印象がつかみやすいと思います。

現ホームページもありますが、会社の内容であったりをつかみにくいため、もっとわかりやすく華やかな印象があり信頼できるページのデザインに仕上げたいと考えています。

こちらに「たたき台となる海外のデザイナーによるWebデザイン」と「日本のデザイナーによるフライヤー(完成版)」の画像がありますので、大きく参考になると思いますので、必ずすべての画像を見ていただいてから作業の開始をお願いします。
https://files.norebun.jp/share/folders/83kqpwZTRmvbhaa41xLoyy0cMEFdPZn7?usp=sharing

海外のデザイナーさんは悪くはないのですが、やはり日本のデザインとは異なり、もう少し日本らしいデザインで信頼性を確保したいと思っています。

今回はこの「トップページ」に関して作成をお願いします。
言葉に関しては後から埋めていけますので、ダミーで入れていただければと思います。

私の好きなサイトデザインを挙げておきますので、ご参考まで。
https://www.tovrex.jp/
https://mizu-lab.in/

単なるまねではなく、個性がしっかりと出ていて、求めていたデザインとなる方と一緒に理想のデザインを求めていければ幸いです。

みなさま、どうぞよろしくお願いいたします。
サイトURL
https://www.sorumina.co.jp/
ページ数
1ページ
希望イメージ
シンプル 複雑
単色 カラフル
暗い 明るい
日常 高級
遊び心 厳粛
未来的 伝統的
女性的 男性的
希望する色
青系、水色系
納品ファイル
• 高解像度JPG (.jpg)
• イラストレーター形式 (.ai)
• フォトショップ形式 (.psd)
補足説明
画像ファイルなどは詳細依頼をご確認ください。
■ 選んだ理由

依頼内容に記載した内容だけではなく、弊社のHPやインタビュー記事なども参考にしていただき、会社の方針を汲み取り、デザインに上手く反映していただいた点から選ばさせていただきました。

■ 提案者全員のお礼・コメント

この度は、既にあるデザインの再構成という一般的な依頼内容とは少し毛色が違うご依頼になってしまったにも関わらず、多数のご提案をありがとうございました。
また、ご縁がございましたら、何卒、よろしくお願いいたします。

```html
<!DOCTYPE html>
<html lang="ja">
<head>
<meta charset="utf-8">
<title>ソルミナ | ひとりひとりのためのAI教育</title>
<link rel="stylesheet" href="https://fonts.googleapis.com/css2?family=Montserrat:wght@500;700;800&family=Noto+Sans+JP:wght@400;500;700&display=swap">
<style>
:root{
  --blue:#1b86d6;
  --blue-soft:#d6e8f6;
  --red:#e0332e;
  --yellow:#f2b300;
  --lime:#a9c43a;
  --ink:#333;
  --sub:#777;
  --line:#dcdcdc;
  --gray-bg:#efefef;
  --white:#fff;
}
*{margin:0;padding:0;box-sizing:border-box}
html,body{width:1200px;height:4920px;overflow:hidden}
body{font-family:"Noto Sans JP",sans-serif;color:var(--ink);background:var(--white);position:relative}
.en{font-family:"Montserrat",sans-serif}
section,header,footer{position:relative;width:1200px;overflow:hidden}

/* header + hero */
.hero{height:980px;background:var(--white)}
.brand{position:absolute;left:40px;top:24px;display:flex;align-items:center;gap:12px}
.brand-dot{width:38px;height:38px;border-radius:50%;background:var(--blue)}
.brand-name{font-size:20px;font-weight:700;color:var(--ink);letter-spacing:.12em;line-height:1.1}
.brand-name small{display:block;font-family:"Montserrat",sans-serif;font-size:9px;font-weight:700;letter-spacing:.2em;color:var(--ink)}
.nav{position:absolute;right:40px;top:26px;display:flex}
.nav a{display:block;width:120px;text-align:center;font-size:14px;color:var(--ink);text-decoration:none;font-weight:500;padding-bottom:6px}
.dropdown{position:absolute;left:842px;top:58px;width:226px;background:var(--white);box-shadow:0 2px 10px rgba(0,0,0,.12);padding:14px 18px;font-size:13px;line-height:2.3;z-index:2}
.hero-network{position:absolute;left:0;top:441px;width:1200px;height:520px;
  background:
    radial-gradient(ellipse 420px 240px at 30% 45%,rgba(190,200,210,.55),rgba(255,255,255,0) 70%),
    radial-gradient(ellipse 480px 260px at 72% 55%,rgba(180,195,210,.5),rgba(255,255,255,0) 72%),
    linear-gradient(180deg,#f7f8f9,#eef1f3 60%,#f7f8f9)}
.hero-bigai{position:absolute;right:70px;top:170px;font-family:"Montserrat",sans-serif;font-weight:800;font-size:260px;line-height:1;color:#eeeeee;letter-spacing:-.02em}
.hero-title{position:absolute;left:40px;top:170px;font-family:"Montserrat",sans-serif;font-weight:700;font-size:38px;line-height:64px;letter-spacing:.04em}
.hero-title .b{color:var(--blue)}
.hero-title .r{color:var(--red)}
.hero-rule{position:absolute;left:0;top:440px;width:1200px;height:1px;background:var(--line)}
.hero-lead{position:absolute;left:40px;top:452px;font-size:20px;font-weight:500;letter-spacing:.06em}
.hero-lead em{font-style:normal;color:var(--red)}
.hero-text{position:absolute;left:600px;top:500px;width:560px;font-size:18px;line-height:38px;text-align:right;font-weight:500;letter-spacing:.04em}

/* section titles */
.sec-title{position:absolute;left:0;width:1200px;text-align:center}
.sec-title h2{font-family:"Montserrat",sans-serif;font-weight:700;font-size:40px;color:var(--blue);letter-spacing:.04em}
.sec-title p{font-size:13px;margin-top:6px;letter-spacing:.1em}
.sec-title p::before{content:"";display:block;width:50px;height:2px;background:var(--blue);margin:0 auto 10px}
.btn{position:absolute;left:460px;width:280px;height:60px;background:var(--blue);color:var(--white);font-size:15px;font-weight:500;display:flex;align-items:center;justify-content:center;text-decoration:none;letter-spacing:.06em}

/* mission */
.mission{height:660px;background:var(--gray-bg)}
.mission .sec-title{top:92px}
.cycle{position:absolute;left:0;top:0;width:1200px;height:660px}
.cycle-mk{position:absolute;width:52px;height:52px;margin:-26px 0 0 -26px;border-radius:50%;color:var(--white);font-weight:700;font-size:22px;display:flex;align-items:center;justify-content:center}
.cycle-lbl{position:absolute;line-height:1.25;transform:translateY(-50%)}
.cycle-lbl b{display:block;font-family:"Montserrat",sans-serif;font-weight:700;font-size:24px}
.cycle-lbl span{font-size:12px;color:var(--ink)}
.cycle-lbl.left{text-align:right}
.mission .btn{top:570px}

/* business */
.business{height:1120px;background-color:var(--white);background-image:linear-gradient(#eef3f7 1px,transparent 1px),linear-gradient(90deg,#eef3f7 1px,transparent 1px);background-size:40px 40px}
.business .sec-title{top:160px}
.cards{position:absolute;left:100px;top:280px;width:1000px;display:flex;justify-content:space-between}
.card{width:300px;height:580px;background:var(--white);border:1px solid var(--line);position:relative}
.card-icon{position:absolute;left:40px;top:-30px;width:90px;height:90px;background:var(--white);border:1px solid var(--line);display:flex;align-items:center;justify-content:center}
.card h3{margin:96px 30px 0;font-size:17px;line-height:30px;color:var(--ink);text-align:right;font-weight:700}
.card h3 small{display:block;font-size:13px;color:var(--red);font-weight:500}
.card hr{border:0;border-top:1px solid var(--line);margin:26px 30px 0}
.card p{margin:26px 30px 0;font-size:14px;line-height:30px;color:var(--sub)}
.business .btn{top:950px}

/* seminar */
.seminar{height:920px;background:var(--gray-bg)}
.seminar .sec-title{top:80px}
.slides{position:absolute;left:40px;top:200px;width:1120px;display:flex;gap:20px}
.slide{width:360px;background:var(--white)}
.slide-photo{height:240px}
.slide p{padding:24px 26px;font-size:15px;line-height:32px}
.arrow{position:absolute;top:300px;width:24px;height:40px}
.seminar .btn{top:740px}

/* company */
.company{height:600px;background:var(--white)}
.company .sec-title{top:20px}
.points{position:absolute;left:100px;top:140px;width:1000px;display:flex;justify-content:space-between}
.point{width:300px;text-align:center}
.point-badge{width:100px;height:100px;border-radius:50%;background:#d9b35a;opacity:.55;margin:0 auto}
.point h4{font-size:19px;margin-top:22px;font-weight:700}
.point p{font-size:12px;line-height:22px;color:var(--sub);margin-top:12px;text-align:left;padding:0 20px}
.point-marks{display:flex;gap:14px;margin:14px 20px 0}
.point-marks i{display:block;width:80px;height:22px;background:#c8d6e3}
.info{position:absolute;left:100px;top:390px;width:1000px;display:flex;justify-content:space-between;font-size:12px}
.info table{width:470px;border-collapse:collapse}
.info th{width:100px;text-align:left;font-weight:700;padding:7px 0;border-bottom:1px solid var(--line);vertical-align:top}
.info td{padding:7px 0;border-bottom:1px solid var(--line);line-height:18px}

/* cta */
.cta{height:200px;background:var(--blue);text-align:center;color:var(--white)}
.cta p{padding-top:46px;font-size:16px;letter-spacing:.08em}
.cta a{display:inline-flex;margin-top:22px;width:400px;height:64px;background:var(--white);color:var(--blue);font-size:20px;font-weight:700;align-items:center;justify-content:center;text-decoration:none;letter-spacing:.1em}

/* footer */
.site-footer{height:440px;background:var(--white);border-top:1px solid var(--line)}
.foot-brand{position:absolute;left:100px;top:60px}
.foot-brand .brand{position:static}
.foot-addr{margin-top:20px;font-size:13px;line-height:24px}
.foot-nav{position:absolute;left:600px;top:60px;font-size:13px;line-height:30px;list-style:none}
.foot-nav li.sub{padding-left:14px}
.copy{position:absolute;left:0;bottom:30px;width:1200px;text-align:center;font-size:11px;color:var(--sub)}
</style>
</head>
<body>

<section class="hero">
  <div class="hero-network" role="img" aria-label="点と線で結ばれたネットワーク図形の背景"></div>
  <div class="hero-bigai">AI</div>
  <div class="brand">
    <span class="brand-dot"></span>
    <span class="brand-name">ソルミナ<small>SORUMINA</small></span>
  </div>
  <nav class="nav">
    <a href="#">会社案内</a>
    <a href="#">セミナー</a>
    <a href="#">投資紹介</a>
    <a href="#">お問い合わせ</a>
  </nav>
  <div class="dropdown">短期コース<br>長期コース<br>AI人材育成のエコシステム形成支援</div>
  <h1 class="hero-title"><span class="b">WE PROVIDE</span><br><span class="r">EDUCATION</span><br><span class="b">IN THE BEST STYLE FOR YOU</span></h1>
  <div class="hero-rule"></div>
  <p class="hero-lead">ひとりひとりのための <em>AI</em> 教育を</p>
  <p class="hero-text">株式会社ソルミナは人工知能（AI）における教育と<br>コンサルティングサービスを提供します。<br>人工知能の一種である「機械学習」を現場で<br>導入するためのサービスです。</p>
</section>

<section class="mission">
  <div class="sec-title"><h2>OUR MISSION</h2><p>企業理念</p></div>
  <div class="cycle">
    <svg width="1200" height="660" viewBox="0 0 1200 660" style="position:absolute;left:0;top:0">
      <path d="M476 250 H520 Q540 250 548 270 L556 286" fill="none" stroke="var(--blue)" stroke-width="5" stroke-linecap="round"/>
      <path d="M724 250 H680 Q660 250 652 270 L644 286" fill="none" stroke="var(--yellow)" stroke-width="5" stroke-linecap="round"/>
      <path d="M476 410 H520 Q540 410 548 390 L556 374" fill="none" stroke="var(--red)" stroke-width="5" stroke-linecap="round"/>
      <path d="M724 410 H680 Q660 410 652 390 L644 374" fill="none" stroke="var(--lime)" stroke-width="5" stroke-linecap="round"/>
      <circle cx="600" cy="330" r="62" fill="var(--blue-soft)"/>
    </svg>
    <div class="cycle-mk" style="left:450px;top:250px;background:var(--blue)">ソ</div>
    <div class="cycle-mk" style="left:750px;top:250px;background:var(--yellow)">ル</div>
    <div class="cycle-mk" style="left:450px;top:410px;background:var(--red)">ミ</div>
    <div class="cycle-mk" style="left:750px;top:410px;background:var(--lime)">ナ</div>
    <div class="cycle-lbl left" style="right:788px;top:250px"><b style="color:var(--blue)">PLAN</b><span>教育</span></div>
    <div class="cycle-lbl" style="left:788px;top:250px"><b style="color:var(--yellow)">DO</b><span>課題設定</span></div>
    <div class="cycle-lbl left" style="right:788px;top:410px"><b style="color:var(--red)">ACTION</b><span>組み込み</span></div>
    <div class="cycle-lbl" style="left:788px;top:410px"><b style="color:var(--lime)">CHECK</b><span>学習モデル構築</span></div>
  </div>
  <a class="btn" href="#">企業理念を見る</a>
</section>

<section class="business">
  <div class="sec-title"><h2>BUSINESS</h2><p>事業紹介</p></div>
  <div class="cards">
    <div class="card">
      <div class="card-icon"><svg width="50" height="44" viewBox="0 0 50 44"><rect x="10" y="4" width="36" height="26" fill="none" stroke="var(--blue)" stroke-width="3"/><line x1="28" y1="30" x2="28" y2="42" stroke="var(--blue)" stroke-width="3"/><line x1="16" y1="14" x2="38" y2="14" stroke="var(--blue)" stroke-width="3"/></svg></div>
      <h3><small>機械学習を現場で活かす</small>短期セミナー</h3>
      <hr>
      <p>短期セミナーはここにテキストが入ります。短期セミナーはここにテキストが入ります。短期セミナーはここにテキストが入ります。</p>
    </div>
    <div class="card">
      <div class="card-icon"><svg width="40" height="48" viewBox="0 0 40 48"><path d="M6 4 H34 L20 24 L34 44 H6 L20 24 Z" fill="none" stroke="var(--blue)" stroke-width="3"/></svg></div>
      <h3><small>本格的な機械学習人材へ</small>長期セミナー</h3>
      <hr>
      <p>長期セミナーはここにテキストが入ります。長期セミナーはここにテキストが入ります。長期セミナーはここにテキストが入ります。</p>
    </div>
    <div class="card">
      <div class="card-icon"><svg width="50" height="44" viewBox="0 0 50 44"><rect x="6" y="28" width="8" height="14" fill="var(--blue)"/><rect x="20" y="20" width="8" height="22" fill="var(--blue)"/><rect x="34" y="8" width="8" height="34" fill="var(--blue)"/></svg></div>
      <h3>AI人材育成の<br>エコシステム形成支援</h3>
      <hr>
      <p>AI人材育成のエコシステム形成支援が入ります。AI人材育成のエコシステム形成支援の説明が入ります。</p>
    </div>
  </div>
  <a class="btn" href="#">事業紹介を見る</a>
</section>

<section class="seminar">
  <div class="sec-title"><h2>SEMINAR</h2><p>セミナー</p></div>
  <svg class="arrow" style="left:4px" viewBox="0 0 24 40"><path d="M20 4 L4 20 L20 36" fill="none" stroke="var(--blue)" stroke-width="4"/></svg>
  <svg class="arrow" style="right:4px" viewBox="0 0 24 40"><path d="M4 4 L20 20 L4 36" fill="none" stroke="var(--blue)" stroke-width="4"/></svg>
  <div class="slides">
    <div class="slide"><div class="slide-photo" role="img" aria-label="セミナー会場で講義を受ける受講者の写真" style="background:linear-gradient(135deg,#d7dde3,#9eaab6)"></div><p>【New】自社で作る AI 人材を育成！3ヶ月の長期コース大阪開講！</p></div>
    <div class="slide"><div class="slide-photo" role="img" aria-label="共催セミナーの告知ビジュアル" style="background:linear-gradient(135deg,#e7f1f8,#a9cde8)"></div><p>【大盛況】ノースウィンド × Brightfield Labs × ソルミナ</p></div>
    <div class="slide"><div class="slide-photo" role="img" aria-label="ディープラーニングハンズオンセミナーの写真" style="background:linear-gradient(135deg,#c9ccb8,#7e8a80)"></div><p>【New】ディープラーニングハンズオンセミナー Advanced コース</p></div>
  </div>
  <a class="btn" href="#">セミナー一覧を見る</a>
</section>

<section class="company">
  <div class="sec-title"><h2>COMPANY</h2><p>企業情報</p></div>
  <div class="points">
    <div class="point"><div class="point-badge"></div><h4>大手 AI 企業公認</h4><p>日本ノースウィンド株式会社と Brightfield Labs の公認を受けたトレーニング講座です。</p><div class="point-marks"><i></i><i></i></div></div>
    <div class="point"><div class="point-badge"></div><h4>産業振興機構認定</h4><p>「第四次産業革命スキル習得講座」に第一期に認定。</p><div class="point-marks"><i></i></div></div>
    <div class="point"><div class="point-badge"></div><h4>共同プロジェクト多数</h4><p>データサイエンス人材を育成するプロジェクトに参画中。</p><div class="point-marks"><i></i><i></i></div></div>
  </div>
  <div class="info">
    <table>
      <tr><th>商号</th><td>株式会社ソルミナ</td></tr>
      <tr><th>設立</th><td>2017年1月17日</td></tr>
      <tr><th>事業内容</th><td>機械学習の教育及びコンサルティング</td></tr>
      <tr><th>役員</th><td>5名（パートナー含む）</td></tr>
      <tr><th>資本金</th><td>500,000円</td></tr>
    </table>
    <table>
      <tr><th>代表</th><td>代表取締役 青木 遼</td></tr>
      <tr><th>所在地</th><td>〒108-0023<br>東京都港区芝浦3丁目8-2 ソルミナビル 4F</td></tr>
      <tr><th>取引先</th><td>ノースウィンド日本株式会社<br>Brightfield Labs 株式会社<br>株式会社ミズノハ ホールディングス</td></tr>
    </table>
  </div>
</section>

<section class="cta">
  <p>セミナーへのお申し込みはこちら</p>
  <a href="#">お申込み</a>
</section>

<footer class="site-footer">
  <div class="foot-brand">
    <div class="brand"><span class="brand-dot"></span><span class="brand-name">ソルミナ<small>SORUMINA</small></span></div>
    <p class="foot-addr">〒108-0023<br>東京都港区芝浦3丁目8-2 ソルミナビル 4F<br>TEL 03-5812-4470</p>
  </div>
  <ul class="foot-nav">
    <li>会社案内</li>
    <li>セミナー</li>
    <li class="sub">- 短期コース</li>
    <li class="sub">- 長期コース</li>
    <li class="sub">- AI人材育成のエコシステム形成支援</li>
    <li>お問い合わせ</li>
  </ul>
  <p class="copy en">© SORUMINA Inc. All Rights Reserved.</p>
</footer>

</body>
</html>
```